Business Card Design for a Design/Build Firm

Kestrel Forge Partners, Inc. is a firm providing construction professional project management and architectural design services to an international clientele. Contemporary. "Green" movement aware. Business card to have back design/logo. Cards will be on high gloss paper

Target Market(s)

Building Developers and Owners

Industry/Entity Type

Construction

Requirements
Nice to have
• We really would like to use the acronym "KFP" as main focal point fo card design. Company will be known as KFP.
Should not have
• No globes or abstract images of buildings.

```html
<!DOCTYPE html>
<html lang="en">
<head>
<meta charset="utf-8">
<title>Kestrel Forge Partners, Inc. — Business Card</title>
<link href="https://fonts.googleapis.com/css2?family=Cinzel:wght@400&family=PT+Sans:wght@400&display=swap" rel="stylesheet">
<style>
  :root {
    --stage: #e9e9e9;
    --brand-blue: #0ba1d9;
    --deep-blue: #1c5876;
    --paper: #ffffff;
    --ink-grey: #6b6b6b;
    --rule-grey: #7a7a7a;
  }
  * { margin: 0; padding: 0; box-sizing: border-box; }
  html, body { width: 1200px; height: 900px; overflow: hidden; }
  body { background: var(--stage); position: relative; font-family: "PT Sans", sans-serif; }

  .card { position: absolute; width: 620px; height: 372px; box-shadow: 0 6px 18px rgba(0,0,0,.18); overflow: hidden; }

  /* Front */
  .card--front { left: 70px; top: 60px; background: var(--brand-blue); color: var(--paper); }
  .front__mark { position: absolute; left: 0; right: 0; top: 88px; text-align: center;
    font-family: "Cinzel", serif; font-size: 78px; letter-spacing: 4px; line-height: 1; color: var(--paper); }
  .front__rule { position: absolute; left: 130px; width: 380px; top: 186px; height: 2px; background: var(--paper); }
  .front__name { position: absolute; left: 0; right: 0; top: 198px; text-align: center;
    font-family: "Cinzel", serif; font-size: 20px; letter-spacing: 1px; color: var(--deep-blue); }
  .front__web { position: absolute; left: 0; right: 0; bottom: 48px; text-align: center;
    font-family: "Cinzel", serif; font-size: 17px; text-transform: lowercase; color: var(--paper); }

  /* Back */
  .card--back { left: 510px; top: 468px; background: var(--paper); }
  .back__header { position: absolute; left: 36px; top: 30px; display: flex; align-items: flex-end; gap: 16px; }
  .back__mark { font-family: "Cinzel", serif; font-size: 52px; line-height: 1; color: var(--ink-grey); letter-spacing: 2px; }
  .back__name { font-family: "Cinzel", serif; font-size: 19px; color: var(--brand-blue); padding-bottom: 4px; }

  .person { position: absolute; left: 36px; top: 190px; display: flex; align-items: baseline; gap: 8px; }
  .person__name { font-size: 23px; color: var(--brand-blue); }
  .person__divider { width: 3px; height: 20px; background: var(--rule-grey); align-self: center; }
  .person__title { font-size: 16px; color: var(--ink-grey); }
  .person__rule { position: absolute; left: 30px; top: 222px; width: 390px; height: 3px; background: var(--rule-grey); }

  .contact { position: absolute; font-size: 14px; color: var(--ink-grey); line-height: 1.35; }
  .contact dt { color: var(--brand-blue); float: left; clear: left; margin-right: 8px; }
  .contact dd { margin-bottom: 6px; overflow: hidden; }
  .contact--left { left: 36px; top: 246px; width: 330px; }
  .contact--right { left: 372px; top: 274px; width: 240px; }

  .back__band { position: absolute; left: 0; bottom: 0; width: 620px; height: 40px; }
</style>
</head>
<body>
  <section class="card card--front" aria-label="Card front">
    <div class="front__mark">KFP</div>
    <div class="front__rule"></div>
    <div class="front__name">KESTREL FORGE PARTNERS, INC.</div>
    <div class="front__web">www.kfpartners.com</div>
  </section>

  <section class="card card--back" aria-label="Card back">
    <header class="back__header">
      <span class="back__mark">KFP</span>
      <span class="back__name">KESTREL FORGE PARTNERS, INC.</span>
    </header>

    <div class="person">
      <span class="person__name">Mara Ellison</span>
      <span class="person__divider"></span>
      <span class="person__title">Director</span>
    </div>
    <div class="person__rule"></div>

    <dl class="contact contact--left">
      <dt>address:</dt><dd>2418 Harbor Crest Way, Suite 210<br>Alderton, CA 95380</dd>
      <dt>phone:</dt><dd>555 318 2706</dd>
    </dl>
    <dl class="contact contact--right">
      <dt>email:</dt><dd>mellison@kfpartners.com</dd>
      <dt>website:</dt><dd>www.kfpartners.com</dd>
    </dl>

    <svg class="back__band" viewBox="0 0 620 40" aria-hidden="true">
      <polygon points="0,14 400,30 380,40 0,40" fill="#0ba1d9"/>
      <polygon points="410,30 430,22 620,30 620,40 392,40" fill="#ffffff"/>
      <polygon points="430,24 620,30 620,40 408,40" fill="#6b6b6b"/>
    </svg>
  </section>
</body>
</html>
```